Quillstone Business Card

We need a business card design. We have a logo from a previous Sketchfold project and I am attaching the logo files in jpeg and photoshop.

```html
<!DOCTYPE html>
<html lang="en">
<head>
<meta charset="UTF-8">
<title>Quillstone Business Card</title>
<link href="https://fonts.googleapis.com/css2?family=Lato:wght@400;700&family=Roboto:wght@700&display=swap" rel="stylesheet">
<style>
  :root {
    --stage: #161616;
    --card: #232323;
    --green: #4bb300;
    --white: #ffffff;
  }
  html, body {
    margin: 0;
    padding: 0;
    width: 1200px;
    height: 900px;
    overflow: hidden;
    background: var(--stage);
  }
  .canvas {
    position: relative;
    width: 1200px;
    height: 900px;
  }
  .card {
    position: absolute;
    left: 75px;
    top: 150px;
    width: 1050px;
    height: 600px;
    background: var(--card);
    overflow: hidden;
    box-shadow: 0 20px 50px rgba(0,0,0,0.6);
  }
  .brand {
    position: absolute;
    left: 70px;
    top: 250px;
    display: flex;
    align-items: center;
    gap: 22px;
  }
  .brand-mark {
    width: 56px;
    height: 56px;
    background: var(--green);
  }
  .brand-name {
    font-family: "Roboto", Arial, sans-serif;
    font-weight: 700;
    font-size: 84px;
    letter-spacing: -2px;
    color: var(--white);
    line-height: 1;
  }
  .person {
    position: absolute;
    right: 70px;
    top: 60px;
    text-align: right;
    font-family: "Lato", Arial, sans-serif;
  }
  .person-name {
    color: var(--green);
    font-size: 30px;
    font-weight: 400;
    letter-spacing: 0.5px;
  }
  .person-title {
    color: var(--white);
    font-size: 26px;
    font-weight: 700;
    margin-top: 2px;
  }
  .contacts {
    position: absolute;
    right: 70px;
    top: 210px;
    list-style: none;
    margin: 0;
    padding: 0;
    font-family: "Lato", Arial, sans-serif;
    color: var(--white);
    font-size: 23px;
  }
  .contact {
    display: flex;
    justify-content: flex-end;
    align-items: flex-start;
    gap: 18px;
    margin-bottom: 14px;
    text-align: right;
    line-height: 1.2;
  }
  .contact-icon {
    width: 24px;
    height: 24px;
    flex: none;
    fill: var(--green);
  }
  .rule-green {
    position: absolute;
    left: 0;
    bottom: 50px;
    width: 840px;
    height: 14px;
    background: var(--green);
  }
  .rule-white {
    position: absolute;
    right: 0;
    bottom: 50px;
    width: 160px;
    height: 14px;
    background: var(--white);
  }
</style>
</head>
<body>
<main class="canvas">
  <section class="card">
    <div class="brand">
      <span class="brand-mark"></span>
      <span class="brand-name">Quillstone</span>
    </div>

    <div class="person">
      <div class="person-name">YOUR NAME</div>
      <div class="person-title">Title</div>
    </div>

    <ul class="contacts">
      <li class="contact">
        <span>123 456 789</span>
        <svg class="contact-icon" viewBox="0 0 24 24" aria-hidden="true"><path d="M3 8c0-3 4-4 9-4s9 1 9 4v2h-5V8H8v2H3z"/><path d="M6 12h12l2 8H4z"/></svg>
      </li>
      <li class="contact">
        <span>yourname@quillstone.com</span>
        <svg class="contact-icon" viewBox="0 0 24 24" aria-hidden="true"><path d="M2 5h20v14H2z M4 7l8 6 8-6" fill="none" stroke="#4bb300" stroke-width="2"/></svg>
      </li>
      <li class="contact">
        <span>www.quillstone.com</span>
        <svg class="contact-icon" viewBox="0 0 24 24" aria-hidden="true"><path d="M3 4h18v12H3z" fill="none" stroke="#4bb300" stroke-width="2"/><path d="M8 20h8v-2H8z"/></svg>
      </li>
      <li class="contact">
        <span>P.O. Box 123 Street 1,<br>NY1234</span>
        <svg class="contact-icon" viewBox="0 0 24 24" aria-hidden="true"><path d="M12 2a7 7 0 0 0-7 7c0 5 7 13 7 13s7-8 7-13a7 7 0 0 0-7-7zm0 10a3 3 0 1 1 0-6 3 3 0 0 1 0 6z"/></svg>
      </li>
    </ul>

    <div class="rule-green"></div>
    <div class="rule-white"></div>
  </section>
</main>
</body>
</html>
```